Covid19 Poster for workplaces

Create a poster on how to protect yourself from Corona virus at work.
We are a Kindly Works company. We have just re-branded so we need to fit in with our brand. We like clean and fresh, slightly amusing is ok if it will draw attention but it's an important topic. A4 and A3 please.

Content:

Headline: Lower the risk of COVID 19 in the workplace.

BE WELL

Bring your own cup - don’t share cups and food.
Elbow tap instead of handshakes and kisses
Wash your hands often - with soap.
Elbow or tissues when you cough or sneeze then straight in the bin
Leave your face alone after touching shared surfaces
Leave your bugs at home if you’re feeling unwell.

Call health line if you have a cough, a high temperature and shortness of breath. 0800 472 9160

Based on recommendations from ZPK and QLN

Target Market(s)

Employees - so anyone

Other font styles liked:
• Use the closest font to the brand documents

Requirements
Should not have
• Clip art

```html
<!DOCTYPE html>
<html lang="en">
<head>
<meta charset="utf-8">
<title>Lower the risk of COVID 19 in the workplace</title>
<link href="https://fonts.googleapis.com/css2?family=Open+Sans:wght@600;700;800&display=swap" rel="stylesheet">
<style>
  :root {
    --ink: #231f20;
    --teal: #00aab7;
    --yellow: #ffd400;
    --white: #ffffff;
    --ghost: #1f2b2d;
    --scene-wood: #6b4a3a;
    --scene-yellow: #f2c431;
    --scene-blue: #2d4c93;
    --scene-red: #c8243a;
    --scene-board: #cfe3f2;
    --icon-light: #e6f6f7;
    --icon-mid: #b8dfe4;
    --icon-warm: #e9a37c;
  }
  * { margin: 0; padding: 0; box-sizing: border-box; }
  html, body { width: 849px; height: 1200px; overflow: hidden; background: var(--ink); }
  .poster {
    position: relative; width: 849px; height: 1200px; overflow: hidden;
    background: var(--ink); font-family: "Open Sans", Arial, sans-serif; color: var(--teal);
  }
  .ghost-word {
    position: absolute; font-weight: 800; font-size: 142px; line-height: 1;
    color: var(--ghost); white-space: nowrap; letter-spacing: -2px;
  }
  .ghost-word.left { left: 104px; top: 438px; transform-origin: 0 0; transform: rotate(90deg); }
  .ghost-word.right { left: 746px; top: 928px; transform-origin: 0 0; transform: rotate(-90deg); }

  .headline { position: absolute; left: 42px; top: 58px; font-weight: 700; }
  .headline .lead, .headline .tail { display: block; font-size: 41px; line-height: 1; letter-spacing: -0.3px; }
  .headline .covid { display: block; color: var(--yellow); font-weight: 800; font-size: 80px; line-height: 1; margin: 4px 0 2px -2px; letter-spacing: -1px; }
  .source { position: absolute; left: 46px; top: 239px; color: var(--white); font-weight: 700; font-size: 17px; line-height: 22px; }

  .office-scene {
    position: absolute; left: 440px; top: 0; width: 409px; height: 330px;
    background:
      radial-gradient(ellipse 70px 60px at 80% 30%, rgba(207,227,242,.55), transparent 70%),
      radial-gradient(ellipse 50px 70px at 34% 62%, rgba(242,196,49,.45), transparent 70%),
      radial-gradient(ellipse 40px 80px at 18% 65%, rgba(45,76,147,.45), transparent 70%),
      radial-gradient(ellipse 40px 60px at 78% 55%, rgba(200,36,58,.4), transparent 70%),
      radial-gradient(ellipse 170px 40px at 55% 72%, rgba(107,74,58,.55), transparent 75%),
      radial-gradient(ellipse 200px 160px at 55% 55%, #3a3336, var(--ink) 80%);
  }

  .be-well { position: absolute; left: 198px; top: 340px; font-weight: 800; font-size: 101px; line-height: 1; letter-spacing: -1px; }

  .tips { position: absolute; left: 0; top: 0; width: 849px; list-style: none; }
  .tip { position: absolute; left: 0; width: 849px; }
  .tip-icon {
    position: absolute; left: 194px; width: 92px; height: 92px; border-radius: 50%;
    border: 4px solid var(--teal); box-shadow: inset 0 0 0 3px var(--ink);
    background: radial-gradient(circle at 50% 55%, var(--icon-mid), var(--icon-light) 55%, var(--white) 75%);
  }
  .tip-icon.warm { background: radial-gradient(circle at 50% 55%, var(--icon-warm), #f6dccb 50%, var(--white) 75%); }
  .tip-text { position: absolute; left: 311px; font-weight: 600; font-size: 24px; line-height: 33px; color: var(--teal); white-space: nowrap; }
  .rule { position: absolute; left: 310px; width: 404px; height: 3px; background: var(--white); }

  .footer { position: absolute; left: 0; top: 1066px; width: 849px; height: 134px; }
  .footer svg { position: absolute; left: 0; top: 0; }
  .helpline { position: absolute; left: 52px; top: 1091px; color: var(--white); font-weight: 700; font-size: 18px; line-height: 24px; }
  .phone { position: absolute; left: 50px; top: 1134px; color: var(--white); font-weight: 800; font-size: 42px; line-height: 1.1; }
  .brand { position: absolute; left: 548px; top: 1090px; display: flex; align-items: center; gap: 14px; }
  .brand-dot { width: 50px; height: 50px; border-radius: 50%; background: var(--white); }
  .brand-name { color: var(--white); font-weight: 800; font-size: 30px; line-height: 30px; }
</style>
</head>
<body>
<main class="poster">
  <div class="ghost-word left" aria-hidden="true">BE WELL</div>
  <div class="ghost-word right" aria-hidden="true">BE WELL</div>

  <h1 class="headline">
    <span class="lead">Lower the risk of</span>
    <span class="covid">COVID 19</span>
    <span class="tail">in the workplace</span>
  </h1>
  <p class="source">Based on recommendations<br>from ZPK and QLN</p>

  <div class="office-scene" role="img" aria-label="Illustration of colleagues talking around an office desk with computers, shelves and a pinboard"></div>

  <h2 class="be-well">BE WELL</h2>

  <ul class="tips">
    <li class="tip" style="top:451px">
      <div class="tip-icon warm" role="img" aria-label="Icon of a drink cup and chicken leg"></div>
      <p class="tip-text" style="top:15px">Bring your own cup<br>don’t share cups and food.</p>
    </li>
    <li class="rule" style="top:542px"></li>
    <li class="tip" style="top:548px">
      <div class="tip-icon warm" role="img" aria-label="Icon of a handshake crossed out"></div>
      <p class="tip-text" style="top:15px">Elbow tap instead of<br>handshakes and kisses</p>
    </li>
    <li class="rule" style="top:645px"></li>
    <li class="tip" style="top:647px">
      <div class="tip-icon" role="img" aria-label="Icon of hands being washed with soap"></div>
      <p class="tip-text" style="top:14px">Wash your hands often<br>with soap.</p>
    </li>
    <li class="rule" style="top:737px"></li>
    <li class="tip" style="top:744px">
      <div class="tip-icon warm" role="img" aria-label="Icon of a person sneezing into a tissue"></div>
      <p class="tip-text" style="top:14px">Elbow or tissues when you cough<br>or sneeze then straight in the bin</p>
    </li>
    <li class="rule" style="top:835px"></li>
    <li class="tip" style="top:843px">
      <div class="tip-icon warm" role="img" aria-label="Icon of a person touching their face, crossed out"></div>
      <p class="tip-text" style="top:12px">Leave your face alone<br>after touching shared surfaces</p>
    </li>
    <li class="rule" style="top:932px"></li>
    <li class="tip" style="top:941px">
      <div class="tip-icon" role="img" aria-label="Icon of an unwell person with a scarf and hot drink"></div>
      <p class="tip-text" style="top:10px">Leave your bugs at home<br>if you’re feeling unwell.</p>
    </li>
    <li class="rule" style="top:1038px"></li>
  </ul>

  <div class="footer">
    <svg width="849" height="134" viewBox="0 0 849 134" aria-hidden="true">
      <rect x="0" y="6" width="849" height="128" fill="var(--teal)"/>
      <path d="M0 8 H400 C500 8 540 104 640 106 H849" fill="none" stroke="var(--yellow)" stroke-width="7"/>
    </svg>
  </div>
  <p class="helpline">Call health line if you have a cough,<br>a high temperature and shortness of breath.</p>
  <p class="phone">0800 472 9160</p>
  <div class="brand">
    <span class="brand-dot"></span>
    <span class="brand-name">Kindly<br>Works</span>
  </div>
</main>
</body>
</html>
```